Overseas Property Tax Depreciation

We need a two sided flyer to promote our business and explain what we do. our website is www.tolvexhq.net.
The attached word file is what I would like on an A5 size flyer with one side showing the FAQ and the other the worked example. I would like these formatted much better than the are and in general style of the website. I will attach files for logos as well.

Business

```html
<!DOCTYPE html>
<html lang="en">
<head>
<meta charset="utf-8">
<title>Tidewell Tax Depreciation – Flyer</title>
<link href="https://fonts.googleapis.com/css2?family=Open+Sans:wght@400;600;700&family=Oswald:wght@500;600&family=Arvo:wght@700&display=swap" rel="stylesheet">
<style>
:root{
  --bg:#d9d6d2;
  --green:#1e9a48;
  --green-dark:#157a37;
  --green-light:#2fb35a;
  --orange:#f5a21c;
  --yellow:#ffd21f;
  --gray-text:#6d6e71;
  --ink:#3b3b3b;
  --white:#ffffff;
}
*{box-sizing:border-box;margin:0;padding:0}
html,body{width:1200px;height:867px;overflow:hidden;background:var(--bg);font-family:"Open Sans",Arial,sans-serif}
.sheet{position:absolute;background:var(--white);overflow:hidden;box-shadow:0 2px 8px rgba(0,0,0,.25)}

/* ---------- Worked example side ---------- */
.example{left:75px;top:97px;width:515px;height:758px}
.example-title{position:absolute;left:0;right:0;top:4px;text-align:center;font-family:"Oswald",sans-serif;font-weight:600;color:var(--gray-text);font-size:22px;line-height:1.2}
.example-title small{display:block;font-size:17px;font-weight:500}
.calc{position:absolute;left:23px;top:65px;width:465px;border-collapse:collapse;font-size:10.5px;color:var(--white)}
.calc th{background:var(--orange);font-weight:600;text-align:left;padding:2px 4px;border-left:1px solid var(--white);font-size:11px;line-height:1.1}
.calc thead tr:first-child th:first-child{border-left:0;border-top-left-radius:12px}
.calc thead tr:first-child th:last-child{border-top-right-radius:12px}
.calc thead .units th{font-size:10px;text-align:left;border-top:1px solid var(--white);height:16px}
.calc td{background:var(--green);padding:2px 4px;vertical-align:top;line-height:1.2}
.calc td.num{border-left:1px solid var(--white);white-space:nowrap}
.calc tr.rule td{border-top:1.5px solid var(--white)}
.calc tr.bold td{font-weight:700}
.calc .note{font-style:italic;float:right}
.calc tbody tr:last-child td:first-child{border-bottom-left-radius:12px}
.calc tbody tr:last-child td:last-child{border-bottom-right-radius:12px}
.calc .big{font-size:14px;font-weight:700;vertical-align:middle}
.tagline{position:absolute;left:0;right:0;top:584px;text-align:center;color:var(--orange);font-size:12.5px;letter-spacing:.3px}
.footer{position:absolute;left:23px;right:23px;top:612px;height:70px;display:flex;align-items:center}
.brand{font-weight:600;color:var(--green);line-height:1;display:flex;align-items:center;gap:6px}
.brand-dot{width:12px;height:12px;border-radius:50%;background:var(--orange)}
.footer .brand{font-size:18px;width:172px}
.contact{border-left:1px solid #ccc;padding-left:8px;font-size:8.5px;color:var(--ink);line-height:1.35;width:140px}
.contact b{font-weight:700}
.partner-badge{width:80px;height:38px;border-left:1px solid #ccc;margin-left:12px;display:flex;align-items:center;justify-content:center}
.partner-badge span{display:block;width:50px;height:24px;background:#5b3b86;border-radius:3px}
.seal{margin-left:12px;text-align:center;font-size:6.5px;color:var(--ink)}
.seal span{display:block;width:38px;height:38px;border-radius:50%;border:3px solid #888;background:#f3f3f3;margin:0 auto 2px}

/* ---------- FAQ side ---------- */
.faq{left:607px;top:77px;width:512px;height:778px;font-size:8.6px;color:var(--ink);line-height:1.35}
.hero-photo{position:absolute;right:0;top:0;width:260px;height:140px;background:linear-gradient(135deg,#e9ecef,#c8cdd3 60%,#9aa3ab)}
.title-band{position:absolute;left:0;top:0;width:300px;height:122px;background:linear-gradient(180deg,#f0f0f0,#c9c9c9)}
.title-band h1{position:absolute;left:22px;top:42px;font-family:"Arvo",serif;font-size:24px;line-height:1.15;color:var(--yellow);-webkit-text-stroke:.6px #6b5300;letter-spacing:.3px}
.url-pill{position:absolute;left:290px;top:117px;width:170px;height:26px;border-radius:13px;background:linear-gradient(180deg,#ffc93a,var(--orange));color:#2a2a2a;font-weight:700;font-size:14px;text-align:center;line-height:26px}
.faq .brand{position:absolute;left:24px;top:128px;font-size:20px}
.intro{position:absolute;left:24px;top:176px;width:240px}
.intro h2,.green h2{font-size:11px;font-weight:700;margin-bottom:2px}
.intro h2{color:#333}
.intro p{text-align:justify;margin-bottom:10px;color:#555}
.ticks{list-style:none}
.ticks li{position:relative;padding-left:15px;margin-bottom:6px;text-align:justify}
.ticks li svg{position:absolute;left:0;top:1px;width:10px;height:10px}
.intro-right{position:absolute;left:282px;top:177px;width:210px;color:#555}
.green{position:absolute;left:0;top:398px;width:512px;height:380px;background:var(--green);color:var(--white);border-top:6px solid var(--green-light)}
.green h2{color:var(--yellow);font-size:11.5px;line-height:1.25;margin:0 0 4px}
.green p{text-align:justify;margin-bottom:10px}
.col{position:absolute;top:10px}
.col-left{left:20px;width:240px}
.col-right{left:272px;width:222px;border-left:1px solid var(--green-dark);padding-left:8px}
.green .ticks li{color:var(--white)}
</style>
</head>
<body>

<section class="sheet example" aria-label="Worked example side">
  <h1 class="example-title">Property Tax Depreciation Example<small>3 bed Semi - detached house Dublin, Constructed in 2006</small></h1>

  <table class="calc">
    <colgroup><col style="width:30px"><col><col style="width:54px"><col style="width:52px"><col style="width:78px"></colgroup>
    <thead>
      <tr><th rowspan="2" style="height:46px">Ref</th><th rowspan="2">Description</th><th colspan="2" style="text-align:center">Without Property Tax Depreciation</th><th style="text-align:center">With Property Depreciation Report</th></tr>
      <tr class="units"><th>Euro</th><th>AUD</th><th>AUD</th></tr>
    </thead>
    <tbody>
      <tr class="bold"><td>A</td><td>Rental Income <span class="note" style="font-style:normal;font-weight:400">€1,200 Month</span></td><td class="num">€14,400</td><td class="num">$20,571</td><td class="num">$20,571</td></tr>
      <tr class="rule"><td></td><td>Expenses</td><td class="num"></td><td class="num"></td><td class="num"></td></tr>
      <tr><td>B.</td><td>Annual Interest charged on<br>outstanding Mortgage (4% apr)</td><td class="num"><br>€12,040</td><td class="num"><br>$17,200</td><td class="num"><br>$17,200</td></tr>
      <tr><td>C</td><td>Property agent fees or commission</td><td class="num">€1,200</td><td class="num">$1,714</td><td class="num">$1,714</td></tr>
      <tr><td>D</td><td>Local Property Tax</td><td class="num">€250</td><td class="num">$357</td><td class="num">$357</td></tr>
      <tr><td>E</td><td>Repairs and Maintenance</td><td class="num">€2,000</td><td class="num">$2,857</td><td class="num">$2,857</td></tr>
      <tr><td>F</td><td>Home Insurance</td><td class="num">€450</td><td class="num">$643</td><td class="num">$643</td></tr>
      <tr><td>G</td><td>Cleaning Advertising et..</td><td class="num">€1,500</td><td class="num">$2,143</td><td class="num">$2,143</td></tr>
      <tr class="bold"><td>H</td><td>Property Tax Depreciation</td><td class="num">€0</td><td class="num">$0</td><td class="num">$15,000</td></tr>
      <tr class="rule bold"><td>I</td><td>Total Annual Expenses <span class="note" style="font-weight:400">Total (B to H)</span></td><td class="num">€17,440</td><td class="num">$24,914</td><td class="num">$39,914</td></tr>
      <tr class="rule bold"><td>J</td><td>Annual Rental Loss/Gain <span class="note" style="font-weight:400">(A less I)</span></td><td class="num">-€3,040</td><td class="num">-$4,343</td><td class="num">-$19,343</td></tr>
      <tr class="rule"><td>K</td><td>Your Annual Income from other sources</td><td class="num"></td><td class="num">$180,000</td><td class="num">$180,000L</td></tr>
      <tr><td>L</td><td>Tour Taxable Income after <span class="note" style="float:none;margin-left:22px">(K Plus J)</span><br>Rental Losses/Gains</td><td class="num"></td><td class="num">$175,657</td><td class="num">$160,657</td></tr>
      <tr><td>M</td><td>Your Marginal Income Tax Rate<br>(37% +2% medicare) <b style="margin-left:60px">39%</b></td><td class="num"></td><td class="num"></td><td class="num"></td></tr>
      <tr class="rule"><td>N</td><td>Annual Tax Saving <span class="note" style="float:none;margin-left:20px">(J multiplied by M)</span><br>Foreign Tax Credits</td><td class="num"></td><td class="num">$1,694</td><td class="num">$7,544</td></tr>
      <tr><td>O</td><td>Non-resident Landlord withholding Tax <i>(20% Ireland)</i><br><i>(A multiplied by 20%)</i></td><td class="num"><br>€2,880</td><td class="num"><br>$4,114</td><td class="num"><br>$4,114</td></tr>
      <tr class="bold"><td>P</td><td>Nett Tax Savings <span class="note" style="float:none;margin-left:30px;font-weight:400">(N Plus O)</span></td><td class="num">$5,808</td><td class="num">$11,658</td><td class="num"></td></tr>
      <tr class="rule bold"><td style="height:40px">Q</td><td>Additional Money in your Pocket (Australia)<br>per year due to Property Tax Depreciation</td><td class="num"></td><td class="num big" colspan="2" style="text-align:center">$5,850</td></tr>
    </tbody>
  </table>

  <p class="tagline">TAX DEPRECIATION REPORTS FOR AUSTRALIAN PROPERTIES</p>

  <div class="footer">
    <div class="brand"><span class="brand-dot"></span>Tidewell Tax Depreciation</div>
    <div class="contact">Suite 000, City name,<br>Country name 00000.<br><b>Tel:</b> 000 000 0000<br><b>email:</b> hello@tidewelltax.com</div>
    <div class="partner-badge"><span></span></div>
    <div class="seal"><span></span>Tax agent<br>31870264</div>
  </div>
</section>

<section class="sheet faq" aria-label="FAQ side">
  <div class="hero-photo" role="img" aria-label="Photo of smiling business people looking at a laptop"></div>
  <div class="title-band"><h1>PROPERTY TAX<br>DEPRECIATION</h1></div>
  <div class="url-pill">www.tolvexhq.net</div>
  <div class="brand"><span class="brand-dot"></span>Tidewell Tax Depreciation</div>

  <div class="intro">
    <h2>Why use us?</h2>
    <p>There are several websites out there offering tax depreciation reports for Australian properties but there are very few who are appropriately qualified and approved by the Australian Tax Office (ATO) and offer the necessary Irish expertise. The Quantity Surveyor that prepares your report:</p>
    <ul class="ticks">
      <li><svg viewBox="0 0 10 10"><rect x=".5" y=".5" width="9" height="9" fill="#fff" stroke="#999"/><path d="M2 5l2 2 4-5" fill="none" stroke="#e59a10" stroke-width="1.6"/></svg>is Irish and qualified as a Quantity Surveyor in Ireland.</li>
      <li><svg viewBox="0 0 10 10"><rect x=".5" y=".5" width="9" height="9" fill="#fff" stroke="#999"/><path d="M2 5l2 2 4-5" fill="none" stroke="#e59a10" stroke-width="1.6"/></svg>worked there during the "Celtic Tiger" period when construction costs were quite high.</li>
      <li><svg viewBox="0 0 10 10"><rect x=".5" y=".5" width="9" height="9" fill="#fff" stroke="#999"/><path d="M2 5l2 2 4-5" fill="none" stroke="#e59a10" stroke-width="1.6"/></svg>has detailed knowledge of Irish construction methods and costs over the past 20 years. Irish buildings are generally much more expensive than Australia due to the climate, just think about how many Australian houses you have seen that have double glazing, central heating, insulation etc..</li>
    </ul>
  </div>

  <ul class="ticks intro-right">
    <li><svg viewBox="0 0 10 10"><rect x=".5" y=".5" width="9" height="9" fill="#fff" stroke="#999"/><path d="M2 5l2 2 4-5" fill="none" stroke="#e59a10" stroke-width="1.6"/></svg>has a partnership arrangement with an Irish quantity surveying firm to carry out the property inspections required in most cases to maximize the deductions available.</li>
    <li><svg viewBox="0 0 10 10"><rect x=".5" y=".5" width="9" height="9" fill="#fff" stroke="#999"/><path d="M2 5l2 2 4-5" fill="none" stroke="#e59a10" stroke-width="1.6"/></svg>is a chartered member of the CSIQ.</li>
    <li><svg viewBox="0 0 10 10"><rect x=".5" y=".5" width="9" height="9" fill="#fff" stroke="#999"/><path d="M2 5l2 2 4-5" fill="none" stroke="#e59a10" stroke-width="1.6"/></svg>Maintains the Appropriate Professional Indemnity Insurance.</li>
    <li><svg viewBox="0 0 10 10"><rect x=".5" y=".5" width="9" height="9" fill="#fff" stroke="#999"/><path d="M2 5l2 2 4-5" fill="none" stroke="#e59a10" stroke-width="1.6"/></svg>Is registered with the Tax Practitioners Board. All quantity surveyors who prepare Property Tax Depreciation Schedules are required by the ATO to be registered with the Tax Practitioners Board which checks that the person preparing the reports is suitably qualified and maintains the appropriate professional indemnity insurance. You can check the registration on the TPB website. Our registration number is 31870264.</li>
  </ul>

  <div class="green">
    <div class="col col-left">
      <h2>My property is in Ireland does this make a difference?</h2>
      <p>Division 43 of the Income Tax Assessment Act 1997 which deals with capital works depreciation states that it applies to buildings begun outside Australia after 21 August 1990 Sect 43.20 (1) (b). Your Australian tax return should cover your worldwide income. As long as the property is available to rent back in Ireland you are obliged by the ATO to report any income or loss on that property.</p>
      <h2>Is my property too old?</h2>
      <p>No, if your property was constructed after 1990 you can claim for both the construction cost element and the Plant and equipment. If it was built before then you can still claim the plant and equipment allowance. The easiest thing to do is to contact us with some details on your property and we can make an initial assessment of the possible annual savings.</p>
      <h2>What is Property Depreciation?</h2>
      <p>Just like you claim wear and tear on a car purchased for income producing purposes, you can also claim the depreciation of your investment property against your taxable income.</p>
    </div>
    <div class="col col-right">
      <p>There are 2 types available: depreciation on Plant and Equipment, and depreciation on the cost of construction. Plant and Equipment refers to items within the building like ovens, dishwashers, carpet and blinds etc. Both these costs can be offset against your assessable income.</p>
      <h2>How much will the report cost?</h2>
      <p>Each scenario is different so contact us to obtain a quick quote for your situation. Generally the cost of the report is a fraction of the savings in any one year.</p>
      <ul class="ticks">
        <li><svg viewBox="0 0 10 10"><rect x=".5" y=".5" width="9" height="9" fill="#fff" stroke="#ccc"/><path d="M2 5l2 2 4-5" fill="none" stroke="#e59a10" stroke-width="1.6"/></svg>Our fee is fully tax deductible</li>
        <li><svg viewBox="0 0 10 10"><rect x=".5" y=".5" width="9" height="9" fill="#fff" stroke="#ccc"/><path d="M2 5l2 2 4-5" fill="none" stroke="#e59a10" stroke-width="1.6"/></svg>You do NOT need to get this report done every year so the cost can be spread over several years</li>
      </ul>
      <h2 style="margin-top:10px">I haven't included my property for the past couple of years on my tax return is this a problem?</h2>
      <p>No, in actual fact you could have been missing out on savings for a number of years, you can also use this report to claim a refund from the ATO for up to the past three years.</p>
    </div>
  </div>
</section>

</body>
</html>
```